Flyer für einen ambulanten Pflegedienst
Zielgruppe
Wir sind ein mobiler Pflegedienst und versorgen Patienten in der Häuslichkeit.
Es soll ein hochwertiger Flyer entworfen werden. Tel für Rückfragen 01564207395
Einige bereits erstellte Flyer habe ich bereits hochgeladen.
Aufgabenstellung
Flyer in A4 einmal mittig gefaltet. Da wir zwei Pflegedienste betreiben, soll der Flyer mit zwei verschiedenen Logos und zwei Adrssen gedruckt und entworfen werden. Der Inhalt des Flyers wäre jedoch zwei mal der selbe. beigefügt ist ein Flyer über Behandlungspflege. Die Angaben von diesem Flyer könnten übernommen werden.
Der Flyer soll exklusiv und nicht so sehr
verspielt werden.

```html
<!DOCTYPE html>
<html lang="de">
<head>
<meta charset="utf-8">
<title>Flyer Pflegehaus Lindental</title>
<link href="https://fonts.googleapis.com/css2?family=Lato:wght@400;700&display=swap" rel="stylesheet">
<style>
:root{
  --orange:#f29638;
  --green:#8cc365;
  --green-light:#e4f1d9;
  --grey:#555555;
  --blue:#2c68ad;
  --text:#444444;
  --white:#ffffff;
  --page:#ffffff;
}
*{margin:0;padding:0;box-sizing:border-box}
html,body{width:829px;height:1200px;overflow:hidden;background:var(--page)}
body{font-family:'Lato',sans-serif;color:var(--text);position:relative}
.spread{position:absolute;left:24px;width:1140px;height:805px;transform:scale(0.6842);transform-origin:0 0;overflow:hidden;background:var(--white)}
.spread--outside{top:40px}
.spread--inside{top:603px}
.spread svg.shapes{position:absolute;inset:0;width:1140px;height:805px}
.t{position:absolute;font-size:17.5px;line-height:21px}
.label-light{color:var(--white);font-size:20px}
.phone-top{font-weight:700;font-size:18px;color:var(--text)}
.heading{font-weight:700;font-size:17.5px}
.heading--blue{color:var(--blue)}
.benefits{list-style:none}
.benefits li{position:relative;padding-left:49px;margin-bottom:0;height:0}
.benefit-icon{position:absolute;left:34px;width:40px;height:40px}
.address,.contact{color:var(--text)}
.contact--light{color:var(--white);text-align:right}
.claim{color:var(--white);font-size:20.5px;line-height:24px}
.claim strong{font-weight:700}
.brand{position:absolute;text-align:center;color:var(--green);font-weight:700;font-size:24px;line-height:26px}
.brand-dot{display:block;margin:0 auto 10px;width:64px;height:64px;border-radius:50%;border:5px solid var(--blue)}
.copy p{margin-bottom:21px}
.copy--right{text-align:right}
.phone-big{color:var(--white);font-size:24px;line-height:28px}
</style>
</head>
<body>

<section class="spread spread--outside">
<svg class="shapes" viewBox="0 0 1140 805">
  <defs>
    <linearGradient id="g1" x1="0" y1="0" x2="1" y2="1"><stop offset="0" stop-color="#8cc365"/><stop offset="1" stop-color="#e4f1d9"/></linearGradient>
    <linearGradient id="p-warm" x1="0" y1="0" x2="1" y2="1"><stop offset="0" stop-color="#b8c79a"/><stop offset="1" stop-color="#e8dcd0"/></linearGradient>
    <linearGradient id="p-blue" x1="0" y1="0" x2="1" y2="1"><stop offset="0" stop-color="#e6e3e0"/><stop offset="1" stop-color="#3b64b4"/></linearGradient>
    <linearGradient id="p-skin" x1="0" y1="0" x2="1" y2="1"><stop offset="0" stop-color="#d9b8a0"/><stop offset="1" stop-color="#ece6e0"/></linearGradient>
    <linearGradient id="p-autumn" x1="0" y1="0" x2="1" y2="1"><stop offset="0" stop-color="#d99a3a"/><stop offset="1" stop-color="#d8d2cc"/></linearGradient>
  </defs>
  <path d="M0 0H300V92C200 110 100 140 0 180Z" fill="var(--grey)"/>
  <path d="M540 0H815C835 60 835 160 760 185C700 190 620 120 545 100Z" fill="var(--orange)"/>
  <path d="M1055 115C950 40 780 50 745 120C720 250 730 420 760 545C800 580 900 560 1000 480L1140 350V115Z" fill="url(#g1)"/>
  <path d="M990 360C1060 330 1140 330 1140 330V570C1080 560 1020 520 990 470Z" fill="var(--orange)"/>
  <circle cx="905" cy="305" r="132" fill="var(--white)"/>
  <g role="img" aria-label="Foto: lächelnde Seniorin im Rollstuhl im Park mit Pflegerin">
    <ellipse cx="415" cy="92" rx="137" ry="103" fill="url(#p-warm)"/>
  </g>
  <g role="img" aria-label="Foto: Pflegerin in blauer Kleidung stützt eine Seniorin">
    <path d="M1010 180C1020 130 1080 108 1140 108V365H1000C1010 300 1000 230 1010 180Z" fill="url(#p-blue)"/>
  </g>
  <g role="img" aria-label="Foto: älteres Ehepaar liest gemeinsam">
    <ellipse cx="728" cy="515" rx="143" ry="118" fill="url(#p-blue)"/>
  </g>
  <g role="img" aria-label="Foto: Seniorin und lächelnde Pflegerin Wange an Wange">
    <path d="M900 560C910 510 960 492 1040 492H1140V725C1060 730 960 735 920 700C890 660 890 610 900 560Z" fill="url(#p-skin)"/>
  </g>
  <path d="M230 545C300 515 430 530 520 565C575 590 590 640 590 710H220Z" fill="url(#g1)"/>
  <path d="M220 690C500 700 800 700 1140 710V805H220Z" fill="var(--grey)"/>
  <g role="img" aria-label="Foto: älteres Paar im Herbstpark, er mit orangefarbenem Schal">
    <path d="M0 570C60 545 160 535 210 550C230 620 225 720 200 805H0Z" fill="url(#p-autumn)"/>
  </g>
</svg>
<div class="t label-light" style="left:46px;top:48px">KONTAKT</div>
<div class="t phone-top" style="left:897px;top:36px">Telefon: 038450-274613</div>
<div class="brand" style="left:805px;top:222px;width:200px"><span class="brand-dot"></span>Pflegehaus<br>Lindental</div>
<div class="t heading" style="left:40px;top:202px">Wir unterstützen Sie gerne</div>
<svg class="benefit-icon" style="top:243px;left:34px" viewBox="0 0 40 40"><circle cx="20" cy="20" r="18" fill="none" stroke="var(--green)" stroke-width="3"/><path d="M12 21l6 6 10-12" fill="none" stroke="var(--green)" stroke-width="3.5"/></svg>
<svg class="benefit-icon" style="top:306px;left:34px" viewBox="0 0 40 40"><circle cx="20" cy="20" r="18" fill="none" stroke="var(--green)" stroke-width="3"/><path d="M12 21l6 6 10-12" fill="none" stroke="var(--green)" stroke-width="3.5"/></svg>
<svg class="benefit-icon" style="top:366px;left:34px" viewBox="0 0 40 40"><circle cx="20" cy="20" r="18" fill="none" stroke="var(--green)" stroke-width="3"/><path d="M12 21l6 6 10-12" fill="none" stroke="var(--green)" stroke-width="3.5"/></svg>
<svg class="benefit-icon" style="top:418px;left:34px" viewBox="0 0 40 40"><circle cx="20" cy="20" r="18" fill="none" stroke="var(--green)" stroke-width="3"/><path d="M12 21l6 6 10-12" fill="none" stroke="var(--green)" stroke-width="3.5"/></svg>
<svg class="benefit-icon" style="top:471px;left:34px" viewBox="0 0 40 40"><circle cx="20" cy="20" r="18" fill="none" stroke="var(--green)" stroke-width="3"/><path d="M12 21l6 6 10-12" fill="none" stroke="var(--green)" stroke-width="3.5"/></svg>
<div class="t" style="left:83px;top:243px">Wir helfen Ihnen dabei, möglichst lange im eigenen Zuhause<br>verbleiben zu können</div>
<div class="t" style="left:83px;top:304px">Wir unterstützen kostenlos bei der Beantragung<br>einer Pflegestufe</div>
<div class="t" style="left:83px;top:365px">Wir sorgen für die Vernetzung aller pflegerischen,<br>medizinischen und sozialen Leistungen</div>
<div class="t" style="left:83px;top:426px">Wir schaffen Transparenz für Betroffene und Angehörige</div>
<div class="t" style="left:83px;top:467px">Wir unterstützen Menschen in belastenden Situationen,<br>auch durch psychosoziale Beratung</div>
<div class="t address" style="left:240px;top:603px">VitaMobil – Der ambulante Pflegedienst GmbH<br>Birkenallee 12<br>17168 Lindental</div>
<div class="t contact--light" style="left:280px;top:740px;width:261px">Email: info@vitamobil.de<br>Webseite: www.vitamobil.de</div>
<div class="t claim" style="left:598px;top:733px"><strong>PFLEGE BEDEUTET VERANTWORTUNG</strong><br>WIR KÜMMERN UNS!</div>
</section>

<section class="spread spread--inside">
<svg class="shapes" viewBox="0 0 1140 805">
  <defs>
    <linearGradient id="g2" x1="0" y1="0" x2="1" y2="1"><stop offset="0" stop-color="#8cc365"/><stop offset="1" stop-color="#e4f1d9"/></linearGradient>
    <linearGradient id="q-room" x1="0" y1="0" x2="1" y2="1"><stop offset="0" stop-color="#c9c3b8"/><stop offset="1" stop-color="#eeeae4"/></linearGradient>
    <linearGradient id="q-blue" x1="0" y1="0" x2="1" y2="1"><stop offset="0" stop-color="#e8e4dc"/><stop offset="1" stop-color="#3a66b6"/></linearGradient>
    <linearGradient id="q-skin" x1="0" y1="0" x2="1" y2="1"><stop offset="0" stop-color="#e3cbb8"/><stop offset="1" stop-color="#b8bcc4"/></linearGradient>
  </defs>
  <path d="M240 0H1140V125C1050 110 960 95 880 80L600 40Z" fill="var(--grey)"/>
  <path d="M390 110C420 60 470 10 530 0H385C380 40 385 80 390 110Z" fill="var(--orange)"/>
  <path d="M665 0H820C835 70 815 170 720 185C690 180 700 130 710 90C710 40 690 20 665 0Z" fill="var(--orange)"/>
  <circle cx="583" cy="95" r="108" fill="var(--white)"/>
  <g role="img" aria-label="Foto: lachendes älteres Ehepaar zu Hause">
    <path d="M0 0H260C250 70 200 130 120 138C60 140 20 125 0 115Z" fill="url(#q-room)"/>
  </g>
  <g role="img" aria-label="Foto: Pflegerin in blauer Kleidung stützt eine Seniorin">
    <path d="M985 55C1040 30 1100 30 1140 30V270C1080 290 1000 290 962 260C950 190 950 100 985 55Z" fill="url(#q-blue)"/>
  </g>
  <path d="M1140 345C1080 350 1040 370 1030 420C1015 500 1000 600 990 690H1140Z" fill="url(#g2)"/>
  <path d="M0 345C100 355 180 380 220 420V640H0Z" fill="var(--green-light)"/>
  <g role="img" aria-label="Foto: lächelnde Seniorin mit kurzem weißen Haar">
    <path d="M0 390C60 370 170 375 215 430C225 520 215 600 180 640H0Z" fill="url(#q-skin)"/>
  </g>
  <path d="M230 690C500 690 800 705 1140 670V805H230Z" fill="var(--grey)"/>
  <path d="M0 650C40 610 120 600 200 605C260 615 290 660 285 710C280 750 255 790 235 805H0Z" fill="var(--orange)"/>
  <g role="img" aria-label="Foto: fröhliches älteres Paar Kopf an Kopf">
    <path d="M660 700C690 640 780 625 860 650C930 670 980 730 990 805H645C640 770 645 730 660 700Z" fill="url(#q-blue)"/>
  </g>
</svg>
<div class="brand" style="left:483px;top:18px;width:200px"><span class="brand-dot"></span>Pflegehaus<br>Lindental</div>
<div class="t heading heading--blue" style="left:19px;top:166px">Ihr mobiler Pflegedienst</div>
<div class="t copy" style="left:19px;top:206px;width:540px">
  <p>Wenn ein hilfsbedürftiger Mensch und dessen Angehörige in einer Pflegesituation Hilfe benötigen, stellen sich viele Fragen:</p>
  <p>Wer unterstützt mich im Alltag? Wie kann ich mein bisheriges Leben in vertrauter Atmosphäre weiterleben? Wo bekomme ich Hilfsmittel? Welche Anträge muss ich stellen?</p>
</div>
<div class="t copy copy--right" style="left:222px;top:360px;width:328px;line-height:24.5px">
  <p>Auf diese und andere Fragen bekommen Sie bei Ihrem mobilen Pflegedienst VitaMobil eine Antwort. Wir kümmern uns darum, dass Sie so lange wie möglich in Ihren eigenen vier Wänden bleiben können.</p>
  <p>Gerne informieren wir Sie zu dem umfassenden Thema Pflege und Betreuung. Wir vermitteln Kontakte zu Ehrenamtlichen oder Angehörigengruppen und haben ein offenes Ohr für Ihre Sorgen und Probleme.</p>
</div>
<div class="t heading heading--blue" style="left:589px;top:231px">weiterer Text</div>
<div class="t copy" style="left:589px;top:270px;width:405px">
  <p>Lorem ipsum dolor sit amet, consectetuer adipiscing elit. Aenean commodo ligula eget dolor. Aenean massa. Cum sociis natoque penatibus et magnis dis parturient montes, nascetur ridiculus mus. Donec quam felis, ultricies nec, pellentesque eu, pretium quis, sem. Nulla consequat massa quis enim.</p>
  <p>Donec pede justo, fringilla vel, aliquet nec, vulputate eget, arcu. In enim justo, rhoncus ut, imperdiet a, venenatis vitae, justo. Nullam dictum felis eu pede mollis pretium. Integer tincidunt. Cras dapibus.</p>
  <p>Vivamus elementum semper nisi. Aenean vulputate eleifend tellus. Aenean leo ligula, porttitor eu, consequat vitae, eleifend ac, enim. Aliquam lorem ante, dapibus in, viverra quis, feugiat a, tellus. Phasellus viverra nulla ut metus varius laoreet.</p>
</div>
<div class="t phone-big" style="left:37px;top:672px">Telefon:<br>038450-274613</div>
<div class="t contact--light" style="left:290px;top:745px;width:260px">Email: info@vitamobil.de<br>Webseite: www.vitamobil.de</div>
</section>

</body>
</html>
```